Breakfast Cafe - The Sunny Perch

It is for my breakfast and lunch cafe with a hawaiian / beach theme. I am open 7 days a week from 7am to 2pm. We serve traditional American food such as omelettes, pancakes, burgers and sandwiches. I'll upload my old card and my new logo to be used. We have a lot of day to day regulars who eat there during the week, our t-shirts actually say 'Locals Only' on them. Hope this helps. Thanks.

Target Market(s)

anyone who has an appetite!

Industry/Entity Type

American Restaurant

Contact Information for Business Card

7340D Marlin Harbor Road
Coral Bay, California
(555) 317-2286

Requirements
Must have
• Address and phone number easily readable.
Nice to have
• beach or tropical theme

```html
<!DOCTYPE html>
<html lang="en">
<head>
<meta charset="utf-8">
<title>The Sunny Perch – Business Card</title>
<link rel="stylesheet" href="https://fonts.googleapis.com/css2?family=Roboto:ital,wght@0,400;0,500;1,500&display=swap">
<style>
  :root {
    --stage: #222221;
    --card-front: #b06212;
    --card-back: #eeeeee;
    --ink-light: #ffffff;
    --rule: #d9954f;
    --accent: #b06212;
  }
  * { margin: 0; padding: 0; box-sizing: border-box; }
  html, body {
    width: 1064px; height: 1200px; overflow: hidden;
    background: var(--stage);
    font-family: "Roboto", Arial, sans-serif;
  }
  .canvas { position: relative; width: 1064px; height: 1200px; }

  .card {
    position: absolute;
    width: 630px; height: 390px;
    box-shadow: 3px 4px 4px rgba(0,0,0,0.75);
  }
  .card--front {
    left: 265px; top: 141px;
    background: var(--card-front);
    border-radius: 0 195px 195px 0;
    color: var(--ink-light);
  }
  .card--back {
    left: 234px; top: 584px;
    background: var(--card-back);
    border-radius: 195px 0 0 195px;
  }

  .details { position: absolute; left: 50px; top: 82px; }
  .details__address { font-size: 17.5px; line-height: 22px; }
  .details__rule {
    width: 134px; height: 1px; background: var(--rule);
    margin: 13px 0 15px;
  }
  .details__hours { font-size: 22.5px; line-height: 28px; }
  .details__tagline { font-size: 22px; line-height: 28px; font-style: italic; font-weight: 500; }
  .details__phone { font-size: 25px; line-height: 30px; }
  .details__phone strong { font-weight: 500; }

  .front-name {
    position: absolute;
    left: 492px; top: 194px;
    transform: translate(-50%, -50%) rotate(-90deg);
    white-space: nowrap;
    font-size: 34px; font-weight: 500;
    color: var(--ink-light);
  }

  .menu {
    position: absolute; left: 107px; top: 117px;
    list-style: none;
    color: var(--accent);
    font-size: 22.5px; line-height: 33.5px;
    letter-spacing: 0.3px;
  }

  .brand-name {
    position: absolute; left: 449px; top: 178px;
    transform: translateX(-50%);
    font-size: 30px; font-weight: 500;
    color: var(--accent);
    white-space: nowrap;
  }
</style>
</head>
<body>
<div class="canvas">

  <section class="card card--front">
    <div class="details">
      <p class="details__address">7340D Marlin Harbor Road<br>Coral Bay, California</p>
      <div class="details__rule"></div>
      <p class="details__hours">Breakfast &amp; Lunch 7am - 2pm Daily</p>
      <div class="details__rule"></div>
      <p class="details__tagline">Family owned and operated!</p>
      <div class="details__rule"></div>
      <p class="details__phone"><strong>Phone:</strong> (555) 317-2286</p>
    </div>
    <div class="front-name">The Sunny Perch</div>
  </section>

  <section class="card card--back">
    <ul class="menu">
      <li>OMELETTES</li>
      <li>PANCAKES</li>
      <li>BURGERS</li>
      <li>SANDWICHES</li>
    </ul>
    <p class="brand-name">The Sunny Perch</p>
  </section>

</div>
</body>
</html>
```